Tarjetas de visita para empresa de aluminio

Empresa con mas de 40 años vendiendo perfiles de aluminio.
Somos fábrica y almacén, queremos renovar la tarjeta de presentación de nuestros comerciales dando una imgen innovadora y tecnógica mezclado con la calidez del respeto al medio ambiente.
Añado el logo de la empresa y actual cara trasera de la tarjeta de visita, el logo es el simbolo ML y la marca TORVENIK EXTRUSION, la frase 2extrusion y lacado de aluminio" debe cambiarse por "Diseño, extrusión, lacado, anodizado y mecanizado de precisión de aluminio" o en su defecto incluir todos esos servicios que hacemos o una frase mas pegadiza.

We are an aluminium factory, we produce and stock profiles of aluminium.
we want to renew visit card of our sellers, we are looking for something that show innovation, tecnology and environment respect.
Upload our actual logo and back of visit card, logo ML and brand TORVENIK EXTRUSION must be keept.
Text "Extrusion y lacado de aluminio" must be changed for "Diseño, extrusion, lacado, anodizado y mecanizado de precisión de aluminio" or something like that

```html
<!DOCTYPE html>
<html lang="es">
<head>
<meta charset="utf-8">
<title>Torvenik Extrusion – Tarjetas de visita</title>
<link rel="stylesheet" href="https://fonts.googleapis.com/css2?family=Open+Sans:wght@400;600;700&display=swap">
<style>
  :root {
    --navy: #0b4a82;
    --navy-deep: #063764;
    --navy-light: #1a63a3;
    --silver: #c4c8cc;
    --paper: #f4f5f6;
    --ink: #1d2430;
    --white: #ffffff;
    --stage: #e6e8eb;
  }
  * { box-sizing: border-box; margin: 0; padding: 0; }
  html, body { width: 1200px; height: 900px; overflow: hidden; }
  body {
    background: var(--stage);
    font-family: "Open Sans", Arial, sans-serif;
    display: flex;
    flex-direction: column;
    align-items: center;
    justify-content: center;
    gap: 28px;
  }
  .card {
    position: relative;
    width: 640px;
    height: 414px;
    border-radius: 6px;
    overflow: hidden;
    box-shadow: 0 6px 18px rgba(0,0,0,.18);
  }
  /* Reverse side */
  .card--reverse { background: var(--navy); }
  .brand {
    position: absolute;
    inset: 0;
    display: flex;
    flex-direction: column;
    align-items: center;
    justify-content: center;
    color: var(--white);
  }
  .brand__mark {
    width: 58px; height: 58px;
    border: 3px solid var(--silver);
    border-radius: 50%;
    margin-bottom: 16px;
  }
  .brand__name {
    font-weight: 600;
    font-size: 38px;
    letter-spacing: 3px;
  }
  .brand__tagline {
    margin-top: 10px;
    font-size: 12.5px;
    letter-spacing: 1.4px;
    text-transform: uppercase;
    text-align: center;
    line-height: 1.55;
  }
  /* Contact side */
  .card--contact { background: var(--navy); }
  .card__waves { position: absolute; inset: 0; width: 100%; height: 100%; }
  .card--contact .brand {
    inset: 14px auto auto 70px;
    width: 330px;
    justify-content: flex-start;
  }
  .card--contact .brand__mark { width: 40px; height: 40px; margin-bottom: 10px; }
  .card--contact .brand__name { font-size: 25px; letter-spacing: 2px; }
  .card--contact .brand__tagline { font-size: 8.5px; margin-top: 6px; letter-spacing: 1px; }
  .person {
    position: absolute;
    right: 40px;
    top: 146px;
    width: 300px;
    text-align: right;
    color: var(--white);
  }
  .person__name { font-weight: 600; font-size: 24px; }
  .person__role {
    font-weight: 600; font-size: 17px;
    padding-bottom: 6px;
    border-bottom: 1.5px solid var(--white);
    margin-bottom: 8px;
  }
  .person__line { font-size: 16px; line-height: 1.35; letter-spacing: .5px; }
  .person__line--email { white-space: nowrap; margin-left: -60px; }
  .address {
    position: absolute;
    left: 40px;
    bottom: 24px;
    color: var(--ink);
    font-size: 16px;
    font-style: normal;
    line-height: 1.4;
  }
  .address__web { font-size: 18px; }
  .address__line--small { font-size: 15px; }
</style>
</head>
<body>

  <section class="card card--reverse" aria-label="Reverso de la tarjeta">
    <div class="brand">
      <div class="brand__mark"></div>
      <div class="brand__name">TORVENIK EXTRUSION</div>
      <p class="brand__tagline">Diseño, extrusión, lacado, anodizado y<br>mecanizado de precisión de aluminio</p>
    </div>
  </section>

  <section class="card card--contact" aria-label="Anverso de la tarjeta">
    <svg class="card__waves" viewBox="0 0 640 414" preserveAspectRatio="none" aria-hidden="true">
      <defs>
        <radialGradient id="glow" cx="0.72" cy="0.35" r="0.55">
          <stop offset="0" stop-color="#1f6cb0"/>
          <stop offset="1" stop-color="#0b4a82"/>
        </radialGradient>
      </defs>
      <rect width="640" height="414" fill="url(#glow)"/>
      <path d="M0 170 C200 190 360 350 640 372 L640 414 L0 414 Z" fill="var(--navy-deep)"/>
      <path d="M0 184 C200 204 360 364 640 386 L640 414 L0 414 Z" fill="var(--silver)"/>
      <path d="M0 192 C200 212 360 372 640 394 L640 414 L0 414 Z" fill="var(--paper)"/>
    </svg>

    <div class="brand">
      <div class="brand__mark"></div>
      <div class="brand__name">TORVENIK EXTRUSION</div>
      <p class="brand__tagline">Diseño, extrusión, lacado, anodizado y<br>mecanizado de precisión de aluminio</p>
    </div>

    <div class="person">
      <div class="person__name">Andrés Molina Ortega</div>
      <div class="person__role">Comercial</div>
      <div class="person__line">M: 611 42 07 85</div>
      <div class="person__line">T : 954 18 27 40</div>
      <div class="person__line">F : 954 18 27 41</div>
      <div class="person__line person__line--email">E : amolina@torvenik.com</div>
    </div>

    <address class="address">
      <div class="address__web">www.torvenik.com</div>
      <div>pol. Ind Los Almendros – C/ 4 Nº 12</div>
      <div class="address__line--small">41720 VILLAVERDE DEL RÍO (Sevilla)</div>
      <div class="address__line--small">Apartado de Correos 245</div>
    </address>
  </section>

</body>
</html>
```